Website Revamp for 7K Distributor

Brovin Pte Ltd (http://brovin.com.sg/about.php) is a 7K authorized distributor located in Singapore.

The revamp hopes to move the look & feel of the website from a corporate/industrial feel to one that is more homely/interior-design, so as to attract architects, home-builders, interior-designers with a more up-market design.
Updates

If product images are required, please use images from www.brovin.com.sg. Thanks!

For newsletter signup, just a link at the header will do, as we will be implementing additional profiling fields in the signup form.

Target Market(s)

Hopes to attract architects, home-builders, interior-designers with a more up-market design.

Industry/Entity Type

Industrial

Requirements
Must have
• Refer to brief document

```html
<!DOCTYPE html>
<html lang="en">
<head>
<meta charset="utf-8">
<title>Brovin Pte Ltd</title>
<link href="https://fonts.googleapis.com/css2?family=Arimo:wght@400;700&family=Open+Sans:wght@400;600;700&display=swap" rel="stylesheet">
<style>
:root{
  --green-light:#9bbd3a;
  --green-dark:#5e8a22;
  --grey-bg:#a8a8a8;
  --white:#ffffff;
  --nav-bg:#f2f2f2;
  --nav-line:#d6d6d6;
  --nav-text:#222;
  --home-dark:#2b2b2b;
  --drop-bg:#ebe9e9;
  --drop-hi:#dcd9d9;
  --drop-text:#7a7a7a;
  --heading-blue:#0d4f8e;
  --link-blue:#1a69b8;
  --body-grey:#666;
  --partner-text:#444;
  --frame:#111;
  --news-from:#2a3fd0;
  --news-to:#0ab8f2;
  --field:#3b3f45;
  --btn-from:#ffd23a;
  --btn-to:#f2a100;
  --footer-from:#4aa0d6;
  --footer-to:#1f74b2;
  --footer-text:#0f2a4a;
}
*{margin:0;padding:0;box-sizing:border-box}
html,body{width:1200px;height:1164px;overflow:hidden}
body{
  position:relative;
  font-family:"Arimo",Arial,sans-serif;
  background:linear-gradient(to bottom,var(--green-light) 0,var(--green-light) 140px,var(--green-dark) 140px,var(--green-dark) 490px,var(--green-light) 490px,var(--green-light) 600px,var(--grey-bg) 600px);
}
.abs{position:absolute}
.page{position:absolute;left:120px;top:0;width:961px;height:1164px;background:var(--white)}
.brand{left:135px;top:18px;font:700 44px/1 "Arimo",sans-serif;color:#1560b8;letter-spacing:-1px}
.social{display:flex;gap:6px}
.social span{width:23px;height:23px;background:#cfcfcf;border-radius:3px}
.social span:first-child{background:#333}
.social.top{left:956px;top:12px}
.nav{left:120px;top:101px;width:961px;height:40px;background:var(--nav-bg);border-top:1px solid var(--nav-line);border-bottom:1px solid var(--nav-line);display:flex}
.nav a{font:400 13px/39px "Arimo",sans-serif;color:var(--nav-text);text-decoration:none;text-align:center;border-right:1px solid var(--nav-line)}
.nav a.active{background:linear-gradient(#4a4a4a,var(--home-dark));color:#fff}
.dropdown{left:420px;top:141px;width:152px;box-shadow:2px 2px 3px rgba(0,0,0,.25)}
.dropdown div,.submenu div{height:29px;border-bottom:1px solid #fff;background:var(--drop-bg);font:400 11px/29px "Open Sans",sans-serif;color:var(--drop-text);padding-left:14px;letter-spacing:.2px}
.dropdown .hi{background:var(--drop-hi)}
.submenu{left:572px;top:199px;width:195px;box-shadow:2px 2px 3px rgba(0,0,0,.25)}
.submenu div{padding-left:11px;background:var(--drop-hi)}
.hero{left:120px;top:141px;width:961px;height:348px;background:linear-gradient(100deg,#8b5a2e 0%,#c49a6c 18%,#e9e6e2 45%,#d7d2cc 70%,#b9b2aa 100%)}
.arrow{top:260px;width:30px;height:68px;background:#fff}
.arrow svg{position:absolute;left:7px;top:20px}
.partners{left:120px;top:489px;width:961px;height:111px;background:linear-gradient(#fff,#efefef)}
.partner-name{left:284px;top:524px;display:flex;align-items:center;gap:10px;font:400 30px/1 "Arimo",sans-serif;color:var(--partner-text)}
.partner-name i{display:block;width:22px;height:22px;background:var(--partner-text)}
.partner-line{left:444px;top:528px;font:400 13px/15px "Arimo",sans-serif;color:#222}
.partner-line b{font-weight:400;color:var(--partner-text)}
.badge{left:738px;top:530px;width:190px;height:50px;background:#1b1b1b;border-radius:4px}
.h2{font:400 14px/1 "Open Sans",sans-serif;color:var(--heading-blue);text-transform:uppercase}
.frame{border:6px solid var(--frame)}
.ph-sky{background:linear-gradient(#3d8fd8,#cfe6f8 55%,#5b7d9c)}
.ph-warm{background:linear-gradient(135deg,#6b4a33,#c8a98a)}
.ph-stone{background:linear-gradient(135deg,#5a6a5a,#c9cfc8)}
.ph-room{background:linear-gradient(90deg,#8b8a84,#d8dad6 50%,#9a9890)}
.ph-window{background:linear-gradient(135deg,#7bb7e6,#e9f3f8 60%,#6aa040)}
.link{font:400 11px/1 "Open Sans",sans-serif;color:#1f3fd6;text-decoration:underline}
.text{font:400 11px/16px "Open Sans",sans-serif;color:var(--body-grey);text-align:justify}
.circle{width:21px;height:21px;border-radius:50%;background:linear-gradient(#fff,#ddd);border:1px solid #999}
.newsletter{left:460px;top:848px;width:274px;height:152px;border-radius:4px;background:linear-gradient(120deg,var(--news-from),var(--news-to));box-shadow:0 6px 6px -4px rgba(0,0,0,.4)}
.newsletter h3{position:absolute;left:20px;top:16px;font:700 14px/1 "Open Sans",sans-serif;color:#fff;letter-spacing:.3px}
.field{position:absolute;left:25px;width:223px;height:29px;border-radius:4px;background:linear-gradient(#52565c,var(--field));border:1px solid #222;font:400 12px/27px "Open Sans",sans-serif;color:#fff;padding-left:18px}
.signup{position:absolute;left:166px;top:117px;width:81px;height:28px;border-radius:4px;background:linear-gradient(var(--btn-from),var(--btn-to));border:1px solid #c07a00;font:700 12px/26px "Open Sans",sans-serif;color:#222;text-align:center;letter-spacing:.5px}
.hot{left:759px;top:615px;width:312px;height:386px;border:4px solid #e4e4e4;background:#fff}
.hot-title{position:absolute;left:8px;top:13px;font:400 14px/1 "Open Sans",sans-serif;color:#333}
.tab{position:absolute;left:8px;top:41px;width:93px;height:35px;background:#2a2a2a;font:400 13px/35px "Open Sans",sans-serif;color:#fff;text-align:center}
.tab-line{position:absolute;left:8px;top:73px;width:289px;height:4px;background:#2a2a2a}
.item{position:absolute;left:11px;width:283px;border-bottom:1px dotted #999;padding-bottom:12px}
.item h4{font:400 12px/1 "Open Sans",sans-serif;color:var(--link-blue);margin-bottom:4px;letter-spacing:.3px}
.item p{font:400 11px/18px "Open Sans",sans-serif;color:#555;letter-spacing:.2px}
.hot-more{position:absolute;left:15px;top:356px;font:400 12px/1 "Open Sans",sans-serif;color:var(--link-blue)}
.footer{left:120px;top:1021px;width:961px;height:143px;background:linear-gradient(var(--footer-from),var(--footer-to))}
.footer-links{left:145px;top:1038px;font:400 12px/18px "Arimo",sans-serif;color:var(--footer-text)}
.social.bottom{left:956px;top:1031px}
.social.bottom span{background:#7ab8e0}
.social.bottom span:first-child{background:#1a2a44}
</style>
</head>
<body>
<div class="page"></div>

<div class="abs brand">Brovin</div>
<div class="abs social top" role="img" aria-label="Social links"><span></span><span></span><span></span><span></span></div>

<nav class="abs nav">
  <a class="active" style="width:134px">HOME</a>
  <a style="width:165px">THE PHILOSOPHY</a>
  <a style="width:151px">OUR SOLUTIONS</a>
  <a style="width:152px">OUR PORTFOLIOS</a>
  <a style="width:121px">CONTACT US</a>
</nav>

<div class="abs hero" role="img" aria-label="Modern living room interior with wooden partition and white sofas"></div>
<div class="abs arrow" style="left:125px"><svg width="16" height="28"><path d="M14 2 L2 14 L14 26 Z" fill="#bbb"/></svg></div>
<div class="abs arrow" style="left:1046px"><svg width="16" height="28"><path d="M2 2 L14 14 L2 26 Z" fill="#bbb"/></svg></div>

<div class="abs dropdown">
  <div>GLASS &amp; GLAZING</div>
  <div>BUILDING SERVICES</div>
  <div class="hi">FILTRATION</div>
  <div>AUTOMOTIVES</div>
  <div>OTHER</div>
</div>
<div class="abs submenu">
  <div>HOME USE WATER FILTER</div>
  <div>COMMERCIAL WATER FILTERS</div>
</div>

<div class="abs partners"></div>
<div class="abs partner-name"><i></i>7K</div>
<div class="abs partner-line"><b>7K</b><br>Authorized Distributor<br>Architectural and Interior Solutions</div>
<div class="abs badge" role="img" aria-label="Partner association badge"></div>

<div class="abs h2" style="left:139px;top:622px">Featured Solutuions</div>
<div class="abs frame ph-sky" style="left:140px;top:644px;width:278px;height:110px" role="img" aria-label="Glass towers against blue sky"></div>
<svg class="abs" style="left:166px;top:758px" width="14" height="8"><path d="M0 8 L7 0 L14 8Z" fill="#111"/></svg>
<div class="abs frame ph-sky" style="left:140px;top:765px;width:86px;height:73px" role="img" aria-label="Glass towers"></div>
<div class="abs frame ph-stone" style="left:237px;top:765px;width:86px;height:73px" role="img" aria-label="Film being applied to glass"></div>
<div class="abs frame ph-warm" style="left:334px;top:765px;width:86px;height:73px" role="img" aria-label="Decorative glass panel"></div>
<div class="abs link" style="left:360px;top:846px">View More</div>
<div class="abs ph-room" style="left:140px;top:884px;width:291px;height:116px;box-shadow:0 6px 6px -4px rgba(0,0,0,.4)" role="img" aria-label="Office with frosted glass partition"></div>

<div class="abs h2" style="left:450px;top:622px">Featured Portfolio</div>
<div class="abs frame ph-warm" style="left:451px;top:650px;width:86px;height:72px" role="img" aria-label="Interior project"></div>
<div class="abs frame ph-room" style="left:552px;top:650px;width:86px;height:72px" role="img" aria-label="Window blinds project"></div>
<div class="abs frame ph-window" style="left:653px;top:650px;width:86px;height:72px" role="img" aria-label="Window film project"></div>
<div class="abs circle" style="left:572px;top:728px"><svg width="19" height="19"><path d="M11 5 L7 9.5 L11 14" stroke="#333" stroke-width="2" fill="none"/></svg></div>
<div class="abs circle" style="left:595px;top:728px"><svg width="19" height="19"><path d="M8 5 L12 9.5 L8 14" stroke="#333" stroke-width="2" fill="none"/></svg></div>
<p class="abs text" style="left:451px;top:761px;width:292px">Lorem ipsum dolor sit amet, consectetur adipisicing elit, sed do eiusmod tempor incididunt ut labore et dolore magna aliqua.</p>
<div class="abs link" style="left:451px;top:815px">Learn More</div>

<div class="abs newsletter">
  <h3>Newsletter Signup</h3>
  <div class="field" style="top:40px">Name</div>
  <div class="field" style="top:80px">Email Id</div>
  <div class="signup">Signup</div>
</div>

<div class="abs hot">
  <div class="hot-title">WHATS HOT</div>
  <div class="tab">News</div>
  <div class="tab-line"></div>
  <div class="item" style="top:101px"><h4>lorem ipsum dolar sit amet</h4><p>lorem ipsum dolar site amet lorem ipsum dlola sit amet lorem 31 may 2012 to 03 august 2012</p></div>
  <div class="item" style="top:182px"><h4>lorem ipsum dolar sit amet</h4><p>lorem ipsum dolar site amet lorem ipsum dlola sit amet lorem 31 may 2012 to 03 august 2012</p></div>
  <div class="item" style="top:271px"><h4>lorem ipsum dolar sit amet</h4><p>lorem ipsum dolar site amet lorem ipsum dlola sit amet lorem 31 may 2012 to 03 august 2012</p></div>
  <div class="hot-more">View More ::</div>
</div>

<footer class="abs footer"></footer>
<div class="abs footer-links">Home &nbsp;|&nbsp; About us &nbsp;|&nbsp; Products &nbsp;|&nbsp; Services &nbsp;|&nbsp; Help &nbsp;|&nbsp; Terms Of Services &nbsp;|&nbsp; Privacy Policy<br>© Copyright 2012 Brovin Pte Ltd. All Rights Reserved.</div>
<div class="abs social bottom" role="img" aria-label="Social links"><span></span><span></span><span></span><span></span></div>
</body>
</html>
```